New Business Card Design for a Payroll Concierge Company

I need a new business card design that is simple and includes my current information. I am a payroll concierge company that processes payroll for clients who employ household employees and I also manage my client's personal bills, financial records. I want to include my current logo and a logo for an association (PFHKT) I belong too on the front of my business card. I will include both my all my company logo files and the association logo files.

Target Market(s)

People who hire household employees, nannies, home health aides, butlers, maids, etc for wealthy individuals and senior citizens who need help in the home.

Industry/Entity Type

Financial Service

Contact Information for Business Card

Company logo

Name: Martin L. Vellacourt
Managing Director

Office number: 203-555-0148
Business Cell: 203-555-0173

Website: www.tallywagedesk.net
Email: Martin.Vellacourt@tallywagedesk.com

Company address:

17 Heron Lane
Suite 208
Fernvale,VT 06412

Font styles to use
Serif
Sans Serif

Colors
3176b5
85cae6
cee9f5
33a6d7
d3d3d3
dbdbdb

Requirements
Must have
• I need to have my company logo and name, phone numbers, website, email, and address on the card. I also want the association logo on the card somewhere but not too big. Small enough to see the logo maybe on the top or bottom corner. Or some where on there card that it doesn't take away the design.
Nice to have
• i like the blue color in my logo, grey, please see must haves business card details.
Should not have
• PLEASE DO NOT USE THE BUSINESS CARD DESIGNS IN THE FILES I UPLOADED. I AM NOT INTERESTED IN THAT DESIGN. ALSO THE ADDRESS AND WEBSITE ARE INCORRECT ON THOSE DESIGNS. PLEASE USE THE UPDATED INFO ON BUSINESS CARD DETAILS

```html
<!DOCTYPE html>
<html lang="en">
<head>
<meta charset="utf-8">
<title>Tally Wage Desk — Business Card</title>
<link rel="stylesheet" href="https://fonts.googleapis.com/css2?family=Roboto:wght@300;400;700&display=swap">
<style>
  :root {
    --backdrop: #e4e4e4;
    --card: #1c1d1f;
    --brand-blue: #3176b5;
    --accent-blue: #33a6d7;
    --light-grey: #d3d3d3;
    --mid-grey: #8a8d91;
    --white: #f2f2f2;
  }
  * { box-sizing: border-box; margin: 0; padding: 0; }
  html, body {
    width: 1200px; height: 864px; overflow: hidden;
    background: var(--backdrop);
    font-family: "Roboto", Arial, sans-serif;
  }
  .stage {
    position: relative; width: 1200px; height: 864px;
    display: flex; align-items: center; justify-content: center; gap: 40px;
  }
  .card {
    position: relative; width: 540px; height: 309px;
    background: var(--card);
    border-radius: 3px;
    box-shadow: 0 6px 18px rgba(0,0,0,.25);
    overflow: hidden;
  }

  /* Front */
  .card-front {
    display: flex; flex-direction: column; align-items: center; justify-content: center;
  }
  .wordmark {
    display: flex; align-items: center; gap: 10px;
    color: var(--brand-blue); font-weight: 700; letter-spacing: 1px; white-space: nowrap;
  }
  .wordmark .mark-square {
    width: 22px; height: 22px; background: var(--brand-blue); border-radius: 3px; flex: none;
  }
  .card-front .wordmark { font-size: 34px; }
  .card-front .wordmark .mark-square { width: 28px; height: 28px; }
  .front-web {
    margin-top: 30px; color: var(--mid-grey);
    font-size: 14px; letter-spacing: 3px; font-weight: 300;
  }

  /* Back */
  .association-badge {
    position: absolute; left: 24px; top: 22px;
    width: 60px; height: 30px; background: var(--brand-blue); border-radius: 2px;
  }
  .holder { position: absolute; left: 24px; top: 98px; }
  .holder-name { color: var(--accent-blue); font-size: 17px; font-weight: 400; letter-spacing: .3px; }
  .holder-title { color: var(--white); font-size: 13px; margin-top: 3px; }
  .card-back .wordmark { position: absolute; right: 30px; top: 108px; font-size: 22px; }
  .rule {
    position: absolute; left: 24px; right: 30px; top: 146px; height: 1px; background: var(--white);
  }
  .contacts {
    position: absolute; left: 24px; top: 156px; list-style: none;
    color: var(--white); font-size: 11.5px; line-height: 19px;
  }
  .contacts li { display: flex; align-items: center; gap: 7px; }
  .contacts svg { width: 11px; height: 11px; fill: var(--accent-blue); flex: none; }
  .address {
    position: absolute; right: 30px; bottom: 18px; text-align: right;
    color: var(--white); font-size: 12px; line-height: 16px; font-style: normal;
  }
</style>
</head>
<body>
<main class="stage">
  <section class="card card-front" aria-label="Card front">
    <div class="wordmark"><span class="mark-square"></span>TALLY WAGE DESK</div>
    <p class="front-web">www.tallywagedesk.net</p>
  </section>

  <section class="card card-back" aria-label="Card back">
    <div class="association-badge" role="img" aria-label="Association badge"></div>

    <div class="holder">
      <p class="holder-name">Martin L. Vellacourt</p>
      <p class="holder-title">Managing Director</p>
    </div>

    <div class="wordmark"><span class="mark-square"></span>TALLY WAGE DESK</div>

    <div class="rule"></div>

    <ul class="contacts">
      <li><svg viewBox="0 0 24 24"><path d="M6.6 10.8a15.1 15.1 0 0 0 6.6 6.6l2.2-2.2a1 1 0 0 1 1-.25 11.4 11.4 0 0 0 3.6.6 1 1 0 0 1 1 1V20a1 1 0 0 1-1 1A17 17 0 0 1 3 4a1 1 0 0 1 1-1h3.5a1 1 0 0 1 1 1c0 1.25.2 2.45.6 3.6a1 1 0 0 1-.25 1z"/></svg>203-555-0148</li>
      <li><svg viewBox="0 0 24 24"><path d="M7 1h10a2 2 0 0 1 2 2v18a2 2 0 0 1-2 2H7a2 2 0 0 1-2-2V3a2 2 0 0 1 2-2zm0 3v14h10V4zm5 15.5a1.2 1.2 0 1 0 0 2.4 1.2 1.2 0 0 0 0-2.4z"/></svg>203-555-0173</li>
      <li><svg viewBox="0 0 24 24"><path d="M2 5h20v14H2zm2 2v.5l8 5 8-5V7zm0 2.8V17h16V9.8l-8 5z"/></svg>Martin.Vellacourt@tallywagedesk.com</li>
      <li><svg viewBox="0 0 24 24"><circle cx="12" cy="12" r="10"/></svg>www.tallywagedesk.net</li>
    </ul>

    <address class="address">17 Heron Lane<br>Suite 208<br>Fernvale,VT 06412</address>
  </section>
</main>
</body>
</html>
```